practice letterhead

I need a letterhead design for a new company that is a veterinary specialty company. I am conservative. I want it to look professional - not "cutesy"

I need my name, credentials, address, phone number and website/email on it.

My personal information is as follows: Lorraine Aldous, DVM, DACVIM (Neurology) Certified Veterinary Pain Practitioner (or CVPP) Certified Canine Rehabilitation Therapist (or CCRT) 1487 Marden Hwy Walpole, MA 02317 508-374-6620 lorraine.aldous@kindpawspecialty.com www.kindpawspecialty.com

```html
<!DOCTYPE html>
<html lang="en">
<head>
<meta charset="utf-8">
<title>Kind Paw Veterinary Specialty Center – Stationery</title>
<link rel="stylesheet" href="https://fonts.googleapis.com/css2?family=Arimo:wght@400;700&display=swap">
<style>
  :root {
    --green: #5aab7d;
    --navy: #071c26;
    --ink: #22323a;
    --paper: #ffffff;
    --backdrop: #e6e8e7;
    --rule: #8a9aa1;
  }
  * { box-sizing: border-box; margin: 0; padding: 0; }
  html, body { width: 968px; height: 1200px; overflow: hidden; }
  body { background: var(--backdrop); font-family: "Arimo", Arial, sans-serif; color: var(--green); position: relative; }

  .sheet { position: absolute; left: 44px; top: 40px; width: 880px; height: 1120px; background: var(--paper); box-shadow: 0 4px 18px rgba(0,0,0,.18); overflow: hidden; }
  .sheet .swoosh { position: absolute; left: 0; width: 100%; }
  .sheet .swoosh-top { top: 0; height: 40px; }
  .sheet .swoosh-bottom { bottom: 0; height: 44px; }

  .brand { display: flex; align-items: center; gap: 12px; }
  .brand-dot { border-radius: 50%; background: var(--green); flex: none; }
  .brand-name { font-weight: 700; color: var(--green); line-height: 1.1; }

  .letterhead-header { position: absolute; left: 36px; top: 58px; right: 36px; height: 140px; }
  .letterhead-header .brand { position: absolute; left: 0; top: 24px; }
  .letterhead-header .brand-dot { width: 58px; height: 58px; }
  .letterhead-header .brand-name { font-size: 25px; width: 290px; }
  .letterhead-header .address { position: absolute; left: 118px; top: 118px; font-size: 13px; display: flex; align-items: center; gap: 6px; }

  .contact { position: absolute; right: 40px; top: 0; font-size: 12px; line-height: 1.25; }
  .contact .name { font-weight: 700; font-size: 15px; }
  .contact .name small { font-weight: 400; font-size: 10.5px; }
  .contact .creds { margin-bottom: 8px; }
  .contact .row { display: flex; align-items: center; gap: 7px; margin-top: 4px; font-size: 12.5px; }
  .icon { width: 11px; height: 11px; flex: none; }
  .header-rule { position: absolute; left: 118px; right: 40px; top: 150px; border-top: 1px solid var(--navy); }

  .envelope { position: absolute; left: 116px; top: 300px; width: 640px; height: 290px; border: 1px solid #555; background: var(--paper); overflow: hidden; }
  .envelope svg.bands { position: absolute; inset: 0; width: 100%; height: 100%; }
  .envelope .return { position: absolute; left: 30px; top: 150px; }
  .envelope .brand { gap: 8px; }
  .envelope .brand-dot { width: 26px; height: 26px; }
  .envelope .brand-name { font-size: 11px; width: 130px; }
  .envelope .addr { margin: 4px 0 0 34px; font-size: 10px; line-height: 1.3; }

  .card { position: absolute; top: 700px; width: 352px; height: 214px; overflow: hidden; }
  .card-front { left: 104px; background: var(--paper); border: 1px solid #555; }
  .card-front svg.bands { position: absolute; inset: 0; width: 100%; height: 100%; }
  .card-front .brand { position: absolute; left: 16px; top: 90px; gap: 8px; }
  .card-front .brand-dot { width: 28px; height: 28px; }
  .card-front .brand-name { font-size: 11px; width: 100px; }
  .card-front .divider { position: absolute; left: 154px; top: 40px; height: 150px; border-left: 1px solid var(--green); }
  .card-front .contact { left: 164px; right: auto; top: 44px; font-size: 9px; }
  .card-front .contact .name { font-size: 11px; }
  .card-front .contact .name small { font-size: 7.5px; }
  .card-front .contact .creds { margin-bottom: 12px; }
  .card-front .contact .row { font-size: 8.5px; gap: 5px; margin-top: 5px; }
  .card-front .icon { width: 8px; height: 8px; }

  .card-back { left: 476px; background: var(--navy); display: flex; align-items: center; justify-content: center; }
  .card-back .brand-dot { width: 38px; height: 38px; }
  .card-back .brand-name { font-size: 15px; width: 150px; }
</style>
</head>
<body>
<main class="sheet">
  <svg class="swoosh swoosh-top" viewBox="0 0 880 40" preserveAspectRatio="none" aria-hidden="true">
    <path d="M0 0 H880 V6 Q440 32 0 10 Z" fill="var(--navy)"/>
  </svg>

  <header class="letterhead-header">
    <div class="brand">
      <span class="brand-dot"></span>
      <span class="brand-name">Kind Paw Veterinary<br>Specialty Center</span>
    </div>
    <p class="address">
      <svg class="icon" viewBox="0 0 12 12"><circle cx="6" cy="6" r="6" fill="var(--green)"/><circle cx="6" cy="5" r="2" fill="#fff"/></svg>
      1487 Marden Hwy., Walpole, MA 02317
    </p>
    <div class="contact">
      <p class="name">Lorraine Aldous<small>, DVM, DACVIM (Neurology)</small></p>
      <p class="creds">Certified Veterinary Pain Practitioner<br>Certified Canine Rehabilitation Therapist</p>
      <p class="row"><svg class="icon" viewBox="0 0 12 12"><circle cx="6" cy="6" r="6" fill="var(--green)"/><path d="M4 3.2l1 1.4-.6.7a4 4 0 0 0 2.3 2.3l.7-.6 1.4 1-.6 1c-2.6-.3-4.6-2.3-4.9-4.9z" fill="#fff"/></svg>508-374-6620</p>
      <p class="row"><svg class="icon" viewBox="0 0 12 12"><circle cx="6" cy="6" r="6" fill="var(--green)"/><rect x="3" y="4" width="6" height="4" fill="#fff"/><path d="M3 4l3 2.2L9 4" stroke="var(--green)" stroke-width=".7" fill="none"/></svg>lorraine.aldous@kindpawspecialty.com</p>
      <p class="row"><svg class="icon" viewBox="0 0 12 12"><circle cx="6" cy="6" r="6" fill="var(--green)"/><circle cx="6" cy="6" r="3" fill="none" stroke="#fff" stroke-width=".8"/><path d="M3 6h6M6 3v6" stroke="#fff" stroke-width=".7"/></svg>www.kindpawspecialty.com</p>
    </div>
    <div class="header-rule"></div>
  </header>

  <section class="envelope" aria-label="Envelope">
    <svg class="bands" viewBox="0 0 640 290" preserveAspectRatio="none" aria-hidden="true">
      <path d="M0 112 L270 0 H640 V28 Q330 70 0 112 Z" fill="var(--paper)"/>
      <path d="M0 112 Q330 70 640 28 V34 Q320 90 0 126 Z" fill="var(--navy)"/>
      <path d="M0 290 Q360 270 640 232 V240 Q340 282 0 290 Z" fill="var(--green)"/>
    </svg>
    <div class="return">
      <div class="brand"><span class="brand-dot"></span><span class="brand-name">Kind Paw Veterinary Specialty Center</span></div>
      <p class="addr">1487 Marden Hwy.,<br>Walpole, MA 02317</p>
    </div>
  </section>

  <section class="card card-front" aria-label="Business card front">
    <svg class="bands" viewBox="0 0 352 214" preserveAspectRatio="none" aria-hidden="true">
      <path d="M0 26 Q170 6 352 0 H0 Z" fill="var(--navy)"/>
      <path d="M0 214 Q170 196 352 192 V198 Q180 204 0 214 Z" fill="var(--green)"/>
    </svg>
    <div class="brand"><span class="brand-dot"></span><span class="brand-name">Kind Paw Veterinary Specialty Center</span></div>
    <div class="divider"></div>
    <div class="contact">
      <p class="name">Lorraine Aldous<small>, DVM, DACVIM (Neurology)</small></p>
      <p class="creds">Certified Veterinary Pain Practitioner<br>Certified Canine Rehabilitation Therapist</p>
      <p class="row"><svg class="icon" viewBox="0 0 12 12"><circle cx="6" cy="6" r="6" fill="var(--green)"/><circle cx="6" cy="5" r="2" fill="#fff"/></svg>1487 Marden Hwy., Walpole, MA 02317</p>
      <p class="row"><svg class="icon" viewBox="0 0 12 12"><circle cx="6" cy="6" r="6" fill="var(--green)"/><path d="M4 3.2l1 1.4-.6.7a4 4 0 0 0 2.3 2.3l.7-.6 1.4 1-.6 1c-2.6-.3-4.6-2.3-4.9-4.9z" fill="#fff"/></svg>508-374-6620</p>
      <p class="row"><svg class="icon" viewBox="0 0 12 12"><circle cx="6" cy="6" r="6" fill="var(--green)"/><rect x="3" y="4" width="6" height="4" fill="#fff"/></svg>lorraine.aldous@kindpawspecialty.com</p>
      <p class="row"><svg class="icon" viewBox="0 0 12 12"><circle cx="6" cy="6" r="6" fill="var(--green)"/><circle cx="6" cy="6" r="3" fill="none" stroke="#fff" stroke-width=".8"/></svg>www.kindpawspecialty.com</p>
    </div>
  </section>

  <section class="card card-back" aria-label="Business card back">
    <div class="brand"><span class="brand-dot"></span><span class="brand-name">Kind Paw Specialty</span></div>
  </section>

  <svg class="swoosh swoosh-bottom" viewBox="0 0 880 44" preserveAspectRatio="none" aria-hidden="true">
    <path d="M0 44 Q420 16 880 10 V44 Z" fill="var(--green)"/>
  </svg>
</main>
</body>
</html>
```